flyer for roofing advertising

Need a modern, bold, luxurious advertisement flyer for our roofing company. located in buffalo, ny. Big house with a intense roof design asphalt shingles. slogan is "Reliability starts at the top". Colors varies but want it to be modern. we will be handing these out when we are working in the area. phone number is 716-555-0147 for the NO K.W estimate. also our services are roofing, roof repairs, gutters, attic ventilation. we offer a 15 year warranty with our platinum roof program. We are certified by dwellmatch, harlan trevisk, quarno. Also follow us on linkpage, wexora and frunt. website is ktw-roofing.com, linkpage is ktwroofing. pictures are on linkpage and our website if need more can be provided. also can include a review we have.

```html
<!DOCTYPE html>
<html lang="en">
<head>
<meta charset="utf-8">
<title>KTW Roofing Flyer</title>
<link href="https://fonts.googleapis.com/css2?family=Montserrat:wght@500;600;700;800;900&display=swap" rel="stylesheet">
<style>
  :root {
    --orange: #d9730f;
    --orange-bright: #f28c1b;
    --charcoal: #26292c;
    --slate: #5f6265;
    --icon-grey: #8d9094;
    --ink: #1c1c1c;
    --paper: #ffffff;
    --backdrop: #e4e4e4;
  }
  * { box-sizing: border-box; margin: 0; padding: 0; }
  html, body { width: 1200px; height: 1200px; overflow: hidden; }
  body {
    background: var(--backdrop);
    font-family: "Montserrat", Arial, sans-serif;
    display: flex; align-items: center; justify-content: center;
  }
  .flyer {
    position: relative; width: 848px; height: 1200px;
    background: var(--paper); overflow: hidden;
  }
  .hero-photo {
    position: absolute; left: 0; top: 0; width: 848px; height: 560px;
    background: linear-gradient(160deg, #7fa9dc 0%, #a9c3e0 22%, #8b7f74 45%, #b7ad9b 62%, #8a3b3a 80%, #5a5450 100%);
  }
  .logo-block { position: absolute; left: 0; top: 480px; width: 848px; height: 200px; }
  .brand-name {
    position: absolute; left: 64px; top: 512px;
    font-weight: 900; font-size: 56px; line-height: 1; color: var(--orange-bright);
    letter-spacing: 4px; display: flex; align-items: center; gap: 14px;
  }
  .brand-name .mark { width: 20px; height: 20px; background: var(--orange-bright); }
  .work-photos { position: absolute; left: 540px; top: 410px; width: 308px; height: 630px; }
  .headline {
    position: absolute; left: 36px; top: 640px; line-height: 1;
    font-weight: 900; text-transform: uppercase;
  }
  .headline .lead { font-size: 60px; color: var(--orange); display: block; }
  .headline .sub { font-size: 32px; color: var(--ink); display: block; margin-top: 4px; }
  .services-tab {
    position: absolute; left: 36px; top: 752px; height: 30px; width: 200px;
    background: var(--orange); color: #fff; font-weight: 700; font-size: 16px;
    padding: 6px 16px; clip-path: polygon(0 0, 100% 0, 88% 100%, 0 100%);
  }
  .service-list { position: absolute; list-style: none; }
  .service-list li {
    display: flex; align-items: center; gap: 12px;
    font-weight: 600; font-size: 16px; color: var(--ink); height: 34px; line-height: 1.1;
  }
  .service-list .icon {
    width: 26px; height: 26px; border-radius: 50%; background: var(--icon-grey);
    flex: none; display: flex; align-items: center; justify-content: center;
  }
  .services-main { left: 44px; top: 792px; }
  .services-extra { left: 290px; top: 792px; }
  .services-extra li { height: 46px; }
  .warranty-slab {
    position: absolute; left: 40px; top: 978px; width: 466px; height: 72px;
    background: var(--slate); border: 2px dashed #cfcfcf; outline: 4px solid var(--slate);
    color: #fff; font-weight: 700; font-size: 19px; line-height: 1.3;
    padding: 8px 14px; text-align: center;
  }
  .warranty-slab em { font-style: normal; color: var(--orange-bright); }
  .certified {
    position: absolute; left: 40px; top: 1068px;
    display: flex; align-items: center; gap: 10px;
    font-size: 12px; font-weight: 600; color: var(--ink);
  }
  .badge { display: inline-block; }
  .badge-red { width: 36px; height: 24px; background: #d5262b; }
  .badge-orange { width: 56px; height: 14px; background: #f08a24; border-radius: 7px; }
  .badge-flag { width: 52px; height: 20px; background: #e3101b; transform: skewX(-12deg); }
  .social {
    position: absolute; left: 370px; top: 1060px;
    font-size: 12px; font-weight: 600; color: var(--ink);
  }
  .social-row { display: flex; align-items: center; gap: 5px; margin-top: 4px; }
  .dot { width: 12px; height: 12px; border-radius: 50%; background: #d63c2f; }
  .dot.alt { background: #c41f1f; }
  .dot.blue { background: #3b5a9a; border-radius: 2px; }
  .web-bar { position: absolute; left: 515px; top: 1090px; width: 333px; height: 110px; }
  .call-bar { position: absolute; left: 0; top: 1110px; width: 540px; height: 90px; }
  .call-text {
    position: absolute; left: 36px; top: 1110px; height: 90px;
    display: flex; align-items: center; gap: 16px;
    color: #fff; font-weight: 800;
  }
  .call-text .cta { font-size: 26px; }
  .call-text .phone { font-size: 28px; display: flex; align-items: center; gap: 8px; }
  .web-text {
    position: absolute; left: 565px; top: 1090px; height: 110px;
    display: flex; align-items: center; gap: 10px;
    color: #fff; font-weight: 500; font-size: 17px;
  }
</style>
</head>
<body>
<main class="flyer">
  <div class="hero-photo" role="img" aria-label="Photo of a large house with steep asphalt shingle roofs, dormers with red siding and white trim, under a blue sky"></div>

  <svg class="work-photos" viewBox="0 0 308 630">
    <defs>
      <linearGradient id="tileA" x1="0" y1="0" x2="1" y2="1"><stop offset="0" stop-color="#86acd8"/><stop offset="1" stop-color="#5d5a55"/></linearGradient>
      <linearGradient id="tileB" x1="0" y1="0" x2="1" y2="1"><stop offset="0" stop-color="#6c7077"/><stop offset="1" stop-color="#2f4278"/></linearGradient>
      <linearGradient id="tileC" x1="0" y1="0" x2="1" y2="1"><stop offset="0" stop-color="#dcd6c3"/><stop offset="1" stop-color="#9fb8d6"/></linearGradient>
    </defs>
    <polygon points="50,3 305,3 305,200 14,200" fill="url(#tileA)" stroke="#d9730f" stroke-width="6" role="img" aria-label="Photo of roofers working on a shingle roof"/>
    <polygon points="28,214 305,214 305,412 3,412" fill="url(#tileB)" stroke="#d9730f" stroke-width="6" role="img" aria-label="Photo of gloved hands fitting asphalt shingles"/>
    <polygon points="3,426 305,426 305,627 36,627" fill="url(#tileC)" stroke="#d9730f" stroke-width="6" role="img" aria-label="Photo of a white gutter and downspout under roof eaves"/>
  </svg>

  <svg class="logo-block" viewBox="0 0 848 200" aria-hidden="true">
    <polygon points="0,50 420,0 370,110 0,150" fill="#26292c"/>
  </svg>
  <div class="brand-name"><span class="mark"></span>KTW</div>

  <h1 class="headline"><span class="lead">Reliability</span><span class="sub">Starts at the top</span></h1>

  <div class="services-tab">OUR SERVICES</div>
  <ul class="service-list services-main">
    <li><span class="icon"><svg width="16" height="16" viewBox="0 0 16 16"><path d="M2 8 8 3l6 5v6H2z" fill="none" stroke="#fff" stroke-width="1.6"/></svg></span>Roof Installation</li>
    <li><span class="icon"><svg width="16" height="16" viewBox="0 0 16 16"><path d="M2 4h12v9H2zM2 8h12M6 4v9M10 4v9" fill="none" stroke="#fff" stroke-width="1.4"/></svg></span>Roof Repair</li>
    <li><span class="icon"><svg width="16" height="16" viewBox="0 0 16 16"><circle cx="8" cy="8" r="5" fill="none" stroke="#fff" stroke-width="1.6"/><path d="M8 3v10M3 8h10" stroke="#fff" stroke-width="1.4"/></svg></span>Attic ventilation</li>
    <li><span class="icon"><svg width="16" height="16" viewBox="0 0 16 16"><path d="M2 5h12M2 8h12M2 11h12" stroke="#fff" stroke-width="1.6"/></svg></span>Siding Repair</li>
    <li><span class="icon"><svg width="16" height="16" viewBox="0 0 16 16"><rect x="2" y="3" width="12" height="10" fill="none" stroke="#fff" stroke-width="1.6"/><path d="M2 8h12" stroke="#fff" stroke-width="1.4"/></svg></span>Gutters</li>
  </ul>
  <ul class="service-list services-extra">
    <li><span class="icon"><svg width="16" height="16" viewBox="0 0 16 16"><path d="M2 9 8 3l6 6M4 8v5h8V8" fill="none" stroke="#fff" stroke-width="1.6"/></svg></span>Commercial<br>Roofing</li>
    <li><span class="icon"><svg width="16" height="16" viewBox="0 0 16 16"><path d="M3 12 12 3M9 3h3v3" fill="none" stroke="#fff" stroke-width="1.6"/></svg></span>New Siding<br>Installation</li>
    <li><span class="icon"><svg width="16" height="16" viewBox="0 0 16 16"><circle cx="7" cy="7" r="4" fill="none" stroke="#fff" stroke-width="1.6"/><path d="M10 10l4 4" stroke="#fff" stroke-width="1.8"/></svg></span>Roof<br>Inspection</li>
  </ul>

  <p class="warranty-slab">we offer a <em>15 YEAR</em> warranty with<br>our platinum roof program</p>

  <div class="certified">
    <span>Certified by</span>
    <span class="badge badge-red" aria-label="harlan trevisk preferred contractor badge"></span>
    <span class="badge badge-orange" aria-label="dwellmatch badge"></span>
    <span class="badge badge-flag" aria-label="quarno badge"></span>
  </div>

  <div class="social">
    Follow us:
    <div class="social-row">
      <span class="dot" aria-label="wexora"></span>
      <span class="dot alt" aria-label="frunt"></span>
      <span class="dot blue" aria-label="linkpage"></span>
      <span>ktwroofing</span>
    </div>
  </div>

  <svg class="web-bar" viewBox="0 0 333 110" aria-hidden="true"><polygon points="25,0 333,0 333,110 0,110" fill="#26292c"/></svg>
  <svg class="call-bar" viewBox="0 0 540 90" aria-hidden="true"><polygon points="0,0 540,0 515,90 0,90" fill="#d9730f"/></svg>
  <div class="call-text">
    <span class="cta">Call us today!</span>
    <span class="phone">
      <svg width="26" height="26" viewBox="0 0 24 24"><path d="M6.6 10.8a15 15 0 0 0 6.6 6.6l2.2-2.2a1 1 0 0 1 1-.25 11.4 11.4 0 0 0 3.6.57 1 1 0 0 1 1 1V20a1 1 0 0 1-1 1A17 17 0 0 1 3 4a1 1 0 0 1 1-1h3.5a1 1 0 0 1 1 1c0 1.25.2 2.45.57 3.57a1 1 0 0 1-.25 1z" fill="#26292c"/></svg>
      716-555-0147
    </span>
  </div>

  <div class="web-text">
    <svg width="20" height="20" viewBox="0 0 20 20"><circle cx="10" cy="10" r="8" fill="none" stroke="#d9730f" stroke-width="2"/><path d="M2 10h16M10 2c3 3 3 13 0 16M10 2c-3 3-3 13 0 16" fill="none" stroke="#d9730f" stroke-width="1.5"/></svg>
    www.ktw-roofing.com
  </div>
</main>
</body>
</html>
```